Ashcombe Vista Business Cards

We need business card designs for a modern home development, Ashcombe Vista. We would like to see modern looking designs- clean and simple but striking. I've attached some images of one of the homes so you can see the style of the homes we are putting on the market and perhaps they will inspire your design! I've also attached the logo- both horizontal and vertical. We need to use the logo on the card. I've also attached a sign that has a map of the development. If you can use that and still keep the card nice and clean, great. If not, it's not a problem to leave the map out completely.

```html
<!DOCTYPE html>
<html lang="en">
<head>
<meta charset="utf-8">
<title>Ashcombe Vista Business Cards</title>
<link href="https://fonts.googleapis.com/css2?family=Open+Sans:wght@400;600;700;800&display=swap" rel="stylesheet">
<style>
  :root {
    --canvas: #ecebe8;
    --card-dark: #15252a;
    --map-tone: #1f3136;
    --card-light: #ffffff;
    --ink: #1c2a33;
    --ink-soft: #3a4750;
    --teal: #2b8a9c;
    --on-dark: #e9eef0;
  }
  * { box-sizing: border-box; margin: 0; padding: 0; }
  html, body { width: 1200px; height: 784px; overflow: hidden; }
  body {
    background: var(--canvas);
    font-family: "Open Sans", Arial, sans-serif;
    display: flex;
    align-items: center;
    justify-content: center;
    gap: 40px;
  }
  .card {
    width: 540px;
    height: 309px;
    position: relative;
    box-shadow: 0 6px 18px rgba(0,0,0,0.18);
  }
  /* Back of card */
  .card-back { background: var(--card-dark); }
  .card-back .brand {
    position: absolute;
    top: 22px; left: 0; right: 0;
    display: flex; justify-content: center; align-items: center; gap: 8px;
  }
  .card-back .brand-name { color: var(--on-dark); font-size: 20px; }
  .map-area {
    position: absolute;
    left: 60px; right: 60px; top: 72px; bottom: 40px;
    background: linear-gradient(160deg, #24383d 0%, var(--map-tone) 60%, #1a2b2f 100%);
  }
  /* Shared brand lockup */
  .brand-mark { width: 14px; height: 14px; background: var(--teal); flex: none; }
  .brand-name {
    font-weight: 800;
    text-transform: uppercase;
    letter-spacing: 0.5px;
    line-height: 1;
  }
  /* Front of card */
  .card-front { background: var(--card-light); }
  .card-front .brand {
    position: absolute;
    top: 48px; left: 34px;
    display: flex; align-items: center; gap: 10px;
  }
  .card-front .brand-mark { width: 22px; height: 22px; }
  .card-front .brand-name { color: var(--ink); font-size: 32px; }
  .contact-person { position: absolute; left: 34px; top: 168px; }
  .person-name { color: var(--teal); font-size: 18px; font-weight: 600; }
  .person-role { color: var(--ink); font-size: 10.5px; font-weight: 700; margin-top: 1px; }
  .contact-list { list-style: none; margin-top: 16px; }
  .contact-list li {
    display: flex; align-items: center; gap: 6px;
    color: var(--ink-soft); font-size: 12.5px; line-height: 18px;
  }
  .contact-list svg { width: 12px; height: 12px; fill: var(--teal); flex: none; }
</style>
</head>
<body>
  <section class="card card-back">
    <div class="brand">
      <span class="brand-mark"></span>
      <span class="brand-name">Ashcombe Vista</span>
    </div>
    <div class="map-area" role="img" aria-label="Street map of the Ashcombe Vista development with home lots highlighted"></div>
  </section>

  <section class="card card-front">
    <div class="brand">
      <span class="brand-mark"></span>
      <span class="brand-name">Ashcombe Vista</span>
    </div>
    <div class="contact-person">
      <p class="person-name">Daniel R. Whitford</p>
      <p class="person-role">Developer, Investor</p>
      <ul class="contact-list">
        <li>
          <svg viewBox="0 0 24 24" aria-hidden="true"><path d="M6.6 10.8a15.1 15.1 0 0 0 6.6 6.6l2.2-2.2a1 1 0 0 1 1-.25 11.4 11.4 0 0 0 3.6.57 1 1 0 0 1 1 1V20a1 1 0 0 1-1 1A17 17 0 0 1 3 4a1 1 0 0 1 1-1h3.5a1 1 0 0 1 1 1c0 1.25.2 2.45.57 3.6a1 1 0 0 1-.25 1z"/></svg>
          555.204.3817
        </li>
        <li>
          <svg viewBox="0 0 24 24" aria-hidden="true"><path d="M7 1h10a2 2 0 0 1 2 2v18a2 2 0 0 1-2 2H7a2 2 0 0 1-2-2V3a2 2 0 0 1 2-2zm0 4v13h10V5zm5 14.5a1.2 1.2 0 1 0 0 2.4 1.2 1.2 0 0 0 0-2.4z"/></svg>
          555.318.0462
        </li>
        <li>
          <svg viewBox="0 0 24 24" aria-hidden="true"><path d="M2 5h20v14H2zm2 2v.5l8 5 8-5V7zm0 2.8V17h16V9.8l-8 5z"/></svg>
          dwhitford@mailhub.net
        </li>
        <li>
          <svg viewBox="0 0 24 24" aria-hidden="true"><path d="M12 3l10 9h-3v9h-5v-6h-4v6H5v-9H2z"/></svg>
          2740 Larkspur Lane, Fairview, TX 75069
        </li>
      </ul>
    </div>
  </section>
</body>
</html>
```